Zig Flyer design

I'm after a new family Portrait flyer

It's to be handed out to new parents.

What it must have

must have the photo attached, not heavily cropped.
must have my logo on it and use the color scheme (file attached)
must have my website www.zigmura.com.au
Must have QR code ( file attached)
Must have this tex "

This certificate entitles you to a free portrait session and a Free 8*10 print and $50 credit with Zig. To Validate your Certificate please call 0423108411by the ______________ you will then have 60 days to book a session for your special offer.

This offer is limited to one per family and is not transferable or redeemable for cash.

Please find attached an example of the format of a Flier I like (14cm squared)

Many thanks

Lou

Target Market(s)

The Target market is 25-45 year old middle to upper class people with children or newborns

Requirements
Must have
• must have the photo attached, not heavly cropped as it's a big selling point the photo
must have my logo on it and use the colour scheme
Must have this tex "This certificate entitles you to a free portrait session and a Free 8*10 print and $50 credit with Zig. To Validate your Certificate please call 0423108411by the ____________ you will then have 60 days to book a session for your special offer
must fit in hand well

```html
<!DOCTYPE html>
<html lang="en">
<head>
<meta charset="utf-8">
<title>Zig Flyer design</title>
<link rel="stylesheet" href="https://fonts.googleapis.com/css2?family=Arimo:wght@400&display=swap">
<style>
  :root {
    --paper: #ffffff;
    --ink: #111111;
    --pink: #e8246f;
    --green: #8dc63f;
    --blue: #29abe2;
    --orange: #f7941d;
    --photo-light: #b4b4b4;
    --photo-mid: #777777;
    --photo-dark: #1f1f1f;
    --edge: #d8d8d8;
  }
  * { margin: 0; padding: 0; box-sizing: border-box; }
  html, body {
    width: 1200px;
    height: 655px;
    overflow: hidden;
    background: var(--paper);
  }
  .flyer {
    position: relative;
    width: 1200px;
    height: 655px;
    background: var(--paper);
    font-family: "Arimo", Arial, sans-serif;
    overflow: hidden;
  }
  .family-photo {
    position: absolute;
    left: 0;
    top: 0;
    width: 598px;
    height: 655px;
    border-right: 1px solid var(--edge);
    background:
      radial-gradient(ellipse 40% 50% at 45% 50%, var(--photo-light) 0%, transparent 75%),
      radial-gradient(ellipse 35% 30% at 85% 85%, var(--photo-dark) 0%, transparent 80%),
      radial-gradient(ellipse 30% 35% at 10% 90%, var(--photo-dark) 0%, transparent 80%),
      linear-gradient(170deg, var(--photo-mid) 0%, var(--photo-light) 45%, var(--photo-mid) 75%, var(--photo-dark) 100%);
  }
  .brand {
    position: absolute;
    display: flex;
    align-items: center;
    gap: 12px;
    color: var(--orange);
    line-height: 1;
  }
  .brand-dot {
    display: block;
    border-radius: 50%;
    background: var(--orange);
  }
  .brand--top { left: 432px; top: 22px; font-size: 50px; }
  .brand--top .brand-dot { width: 46px; height: 46px; }
  .brand--bottom { left: 640px; top: 556px; font-size: 62px; }
  .brand--bottom .brand-dot { width: 60px; height: 60px; }
  .offer {
    position: absolute;
    left: 623px;
    top: 38px;
    width: 575px;
    font-size: 34.5px;
    line-height: 54px;
    white-space: nowrap;
  }
  .offer .pink { color: var(--pink); }
  .offer .green { color: var(--green); }
  .offer .blue { color: var(--blue); }
  .offer .ink { color: var(--ink); }
  .date-blank {
    display: inline-block;
    width: 190px;
    height: 26px;
    border-bottom: 2px solid var(--ink);
    vertical-align: baseline;
  }
  .terms {
    position: absolute;
    left: 625px;
    top: 437px;
    font-size: 15px;
    color: var(--orange);
    white-space: nowrap;
  }
  .website {
    position: absolute;
    left: 870px;
    top: 580px;
    font-size: 24px;
    color: var(--ink);
    letter-spacing: 0.5px;
  }
</style>
</head>
<body>
  <main class="flyer">
    <div class="family-photo" role="img" aria-label="Black and white photo of a smiling baby held up in the air by a parent's hands, bare winter trees and sky behind"></div>

    <div class="brand brand--top">
      <span class="brand-dot"></span>
      <span class="brand-name">Zig</span>
    </div>

    <p class="offer">
      <span class="pink">This certificate entitles you to a free</span><br>
      <span class="pink">portrait session and a </span><span class="ink">Free 8*10 print</span><br>
      <span class="ink">and $50 credit with Zig.</span><br>
      <span class="green">To Validate your Certificate please</span><br>
      <span class="green">call </span><span class="ink">0461937205</span><span class="green"> by the </span><span class="date-blank"></span><br>
      <span class="blue">You will then have </span><span class="ink">60 days</span><span class="blue"> to book a</span><br>
      <span class="blue">session for your special offer.</span>
    </p>

    <p class="terms">This offer is limited to one per family and is not transferable or redeemable for cash.</p>

    <div class="brand brand--bottom">
      <span class="brand-dot"></span>
      <span class="brand-name">Zig</span>
    </div>

    <p class="website">www.zigmura.com.au</p>
  </main>
</body>
</html>
```